3 Sympathy Cards for Veterinary Hospital

Hi. Meadowbrook Pet Hospital is a Veterinary Hospital in Australia. We need sympathy cards to send to grieving clients after the loss of their beloved pets.
I have attached the old designs, but we have rebranded and need something to suit our new image.

The cards should have a nice message and appeal to every owner.
They need to match our current branding, but the cards are for the clients, not to advertise us, so not too much branding.
The current cards are attached and they are good because they show a variety of animals so clients might identify with one of them.
I have attached a brown to green gradient that we use on some designs, you don't have to use it, but consider it.
I have attached a logo on background used in some of our new designs, consider using it.
I have attached a font that we use for most new branding.

Target Market(s)

Women 25 to 44

Industry/Entity Type

Veterinary

Font styles to use
Sans Serif
Script

Colors
fac994
cadf82

Requirements
Must have
• IMPORTANT - 3 different designs for the different types of pets.
• 1. Dog.
• 2. Cat.
• 3. Everything else (Rabbits, lizards, ferrets, chickens, birds, mice, rats, snakes)
Nice to have
• Caring and compassionate message.
Should not have
• Too much branding.

```html
<!DOCTYPE html>
<html lang="en">
<head>
<meta charset="utf-8">
<title>Deepest Sympathy Card – Cats</title>
<link href="https://fonts.googleapis.com/css2?family=Dancing+Script:wght@500&family=Roboto+Condensed:wght@400;700&display=swap" rel="stylesheet">
<style>
  :root {
    --backdrop: #515051;
    --card: #d9ddbd;
    --card-fold: #cdd1b0;
    --brown: #5a3a1c;
    --rule: #8c8a73;
    --cream: #efe6d6;
    --ginger: #c98a4e;
    --tabby: #8a7560;
    --dark: #3b2a22;
  }
  * { margin: 0; padding: 0; box-sizing: border-box; }
  html, body { width: 1029px; height: 1200px; overflow: hidden; }
  body { background: var(--backdrop); position: relative; font-family: "Roboto Condensed", sans-serif; }

  .card { position: absolute; left: 226px; top: 202px; width: 576px; height: 796px; }

  .card__back {
    position: absolute; left: 0; top: 0; width: 576px; height: 398px;
    background: var(--card); border-bottom: 1px solid var(--card-fold);
  }
  .back-credit {
    position: absolute; left: 0; top: 72px; width: 576px;
    text-align: center; transform: rotate(180deg); color: var(--brown);
  }
  .back-credit__name {
    font-weight: 700; font-size: 15px; letter-spacing: 0.5px; line-height: 1.1;
    display: flex; align-items: center; justify-content: center; gap: 6px;
  }
  .back-credit__mark { width: 9px; height: 9px; background: var(--brown); }
  .back-credit__legal { font-size: 7.5px; margin-top: 8px; line-height: 1.4; }

  .card__front {
    position: absolute; left: 0; top: 398px; width: 576px; height: 398px;
    background: var(--card);
  }
  .photo-strip {
    position: absolute; display: flex; border: 2px solid var(--brown); background: var(--brown); gap: 2px;
  }
  .photo-strip .photo { flex: 1; height: 100%; }
  .strip-top-left { left: 22px; top: 32px; width: 246px; height: 80px; }
  .strip-top-right { left: 302px; top: 32px; width: 245px; height: 80px; }
  .strip-bottom-left { left: 32px; top: 298px; width: 236px; height: 76px; }
  .strip-bottom-right { left: 301px; top: 298px; width: 236px; height: 76px; }

  .photo--kitten-cream { background: linear-gradient(135deg, var(--dark), #e6d8c8 60%, #6a5a6a); }
  .photo--fluffy-cat { background: linear-gradient(160deg, var(--dark), #c9a27a 55%, #3a2418); }
  .photo--tabby-kitten { background: linear-gradient(135deg, #f2f2f0, var(--tabby) 55%, #e8e4de); }
  .photo--tabby-cat { background: linear-gradient(135deg, #e9ddd0, #9c7b5c 60%, #4a3a2c); }
  .photo--sleeping-pair { background: linear-gradient(160deg, #6a4a34, var(--ginger) 45%, var(--cream)); }
  .photo--calico { background: linear-gradient(160deg, #f4f0ea, #3a3230 50%, var(--cream)); }
  .photo--ginger-cat { background: linear-gradient(135deg, #f0e6da, var(--ginger) 55%, #e9dccb); }
  .photo--ginger-kitten { background: linear-gradient(135deg, #f4ece2, #d69a5e 55%, #b0b8a8); }

  .rule { position: absolute; height: 1px; background: var(--rule); }
  .rule--upper { left: 26px; top: 138px; width: 514px; }
  .rule--lower { left: 32px; top: 273px; width: 498px; }

  .card-title {
    position: absolute; left: 0; top: 162px; width: 576px; text-align: center;
    font-family: "Dancing Script", cursive; font-weight: 500; font-size: 62px;
    color: var(--brown); line-height: 1;
  }
</style>
</head>
<body>
  <div class="card">
    <section class="card__back">
      <div class="back-credit">
        <div class="back-credit__name"><span class="back-credit__mark"></span>MEADOWBROOK PET HOSPITAL</div>
        <p class="back-credit__legal">Copyright 2013 Veterinary supplies<br>P.O Box 218, Fairview 4100 | Ph 1800 555 014</p>
      </div>
    </section>

    <section class="card__front">
      <div class="photo-strip strip-top-left">
        <div class="photo photo--kitten-cream" role="img" aria-label="Photo of a cream kitten on a plaid blanket"></div>
        <div class="photo photo--fluffy-cat" role="img" aria-label="Photo of a fluffy long-haired cat"></div>
      </div>
      <div class="photo-strip strip-top-right">
        <div class="photo photo--tabby-kitten" role="img" aria-label="Photo of a tabby kitten looking ahead"></div>
        <div class="photo photo--tabby-cat" role="img" aria-label="Photo of a tabby cat with a blue collar"></div>
      </div>

      <div class="rule rule--upper"></div>
      <h1 class="card-title">Deepest Sympathy</h1>
      <div class="rule rule--lower"></div>

      <div class="photo-strip strip-bottom-left">
        <div class="photo photo--sleeping-pair" role="img" aria-label="Photo of two cats sleeping together"></div>
        <div class="photo photo--calico" role="img" aria-label="Photo of a calico cat resting"></div>
      </div>
      <div class="photo-strip strip-bottom-right">
        <div class="photo photo--ginger-cat" role="img" aria-label="Photo of a ginger cat lying down"></div>
        <div class="photo photo--ginger-kitten" role="img" aria-label="Photo of a ginger kitten sitting"></div>
      </div>
    </section>
  </div>
</body>
</html>
```